Cedar Harbor Business Cards For New Startup

I am looking for you to design some business cards for a new startup https://cedarharborhub.com. I have supplied logo, brand guidelines and our signatures as a guide.

We need this to reflect the brand guidelines and the website for brand consistency,

What is Cedar Harbor?

Mallorca's Business Growth Community
Join your new business community full of passionate entrepreneurs who
love to solve problems and help each other grow together!

Any questions you can ask.

Target Market(s)

Business to Business

Contact Information for Business Card

These are attached (signatures) to the job

Font styles to use
Other font styles liked:
• Open Sans

Requirements
Must have
• Match design guidelines
Nice to have
• Photos of our faces so people remember us

```html
<!DOCTYPE html>
<html lang="en">
<head>
<meta charset="utf-8">
<title>Cedar Harbor Business Cards</title>
<link href="https://fonts.googleapis.com/css2?family=Open+Sans:ital,wght@0,400;0,700;1,400&display=swap" rel="stylesheet">
<style>
  :root {
    --olive: #666600;
    --white: #ffffff;
    --backdrop: #3a3a3c;
    --photo-top: #e9e6e2;
    --photo-mid: #c49e86;
    --photo-low: #3e5272;
  }
  html, body {
    margin: 0;
    width: 1200px;
    height: 1000px;
    overflow: hidden;
    background: var(--backdrop);
    font-family: "Open Sans", Arial, sans-serif;
  }
  .canvas {
    position: relative;
    width: 1200px;
    height: 1000px;
  }
  .card {
    position: absolute;
    left: 240px;
    width: 720px;
    height: 412px;
    border-radius: 30px;
    overflow: hidden;
  }
  .card--front {
    top: 48px;
    background: var(--olive);
    display: flex;
    align-items: center;
    justify-content: center;
  }
  .card--back {
    top: 540px;
    background: var(--white);
  }
  .brand {
    display: flex;
    align-items: center;
    gap: 26px;
    font-weight: 400;
    letter-spacing: 1px;
  }
  .brand__dot {
    border-radius: 50%;
    border: 2px solid currentColor;
    box-sizing: border-box;
  }
  .card--front .brand { color: var(--white); font-size: 50px; }
  .card--front .brand__dot { width: 92px; height: 92px; }

  .back__band {
    position: absolute;
    inset: 0 0 auto 0;
    height: 128px;
    background: var(--olive);
    color: var(--white);
    padding: 34px 0 0 38px;
    box-sizing: border-box;
  }
  .person__name {
    margin: 0;
    font-size: 30px;
    font-weight: 700;
    line-height: 1.1;
  }
  .person__title {
    margin: 4px 0 0;
    font-size: 18px;
    font-style: italic;
    font-weight: 400;
  }
  .back__body {
    position: absolute;
    left: 38px;
    top: 150px;
    color: var(--olive);
  }
  .card--back .brand { font-size: 36px; gap: 18px; }
  .card--back .brand__dot { width: 66px; height: 66px; }
  .contact {
    list-style: none;
    margin: 18px 0 0;
    padding: 0;
    font-size: 19px;
    line-height: 27px;
  }
  .contact li { display: flex; align-items: center; gap: 10px; }
  .contact svg { width: 15px; height: 15px; flex: none; }
  .contact__web { font-weight: 700; }
  .contact__web span { font-weight: 400; }
  .social {
    display: flex;
    gap: 9px;
    margin-top: 12px;
  }
  .social__dot {
    width: 30px;
    height: 30px;
    border-radius: 50%;
    background: var(--olive);
  }
  .portrait {
    position: absolute;
    right: 0;
    top: 100px;
    width: 300px;
    height: 312px;
    background: linear-gradient(180deg, var(--photo-top) 0%, var(--photo-mid) 30%, var(--photo-mid) 62%, var(--photo-low) 82%, var(--photo-low) 100%);
  }
</style>
</head>
<body>
<main class="canvas">
  <section class="card card--front" aria-label="Card front">
    <div class="brand">
      <span class="brand__dot"></span>
      <span class="brand__name">CEDAR HARBOR</span>
    </div>
  </section>

  <section class="card card--back" aria-label="Card back">
    <header class="back__band">
      <h1 class="person__name">Marcus Delane</h1>
      <p class="person__title">Founder &amp; Growth Hacker | Cedar Harbor</p>
    </header>

    <div class="portrait" role="img" aria-label="Portrait photo of the founder in a blue blazer"></div>

    <div class="back__body">
      <div class="brand">
        <span class="brand__dot"></span>
        <span class="brand__name">CEDAR HARBOR</span>
      </div>
      <ul class="contact">
        <li>
          <svg viewBox="0 0 16 16" aria-hidden="true"><path fill="currentColor" d="M3 1l3 3-1.6 1.8c.8 1.8 2.2 3.2 4 4L10.2 8l3 3-1.8 2.6C6.5 13.2 2.8 9.5 1 4.4z"/></svg>
          +34 611 482 907
        </li>
        <li>
          <svg viewBox="0 0 16 16" aria-hidden="true"><rect x="1" y="3" width="14" height="10" rx="1" fill="currentColor"/><path d="M1.5 3.8L8 9l6.5-5.2" stroke="#fff" stroke-width="1.3" fill="none"/></svg>
          md@cedarharborhub.com
        </li>
        <li>
          <svg viewBox="0 0 16 16" aria-hidden="true" fill="none" stroke="currentColor" stroke-width="1.4"><circle cx="8" cy="8" r="6.5"/><ellipse cx="8" cy="8" rx="3" ry="6.5"/><path d="M1.5 8h13"/></svg>
          cedarharborhub.com
        </li>
        <li class="contact__web">cedarharborhub<span>.com</span></li>
      </ul>
      <div class="social" aria-label="Social profiles">
        <span class="social__dot"></span>
        <span class="social__dot"></span>
        <span class="social__dot"></span>
        <span class="social__dot"></span>
        <span class="social__dot"></span>
      </div>
    </div>
  </section>
</main>
</body>
</html>
```